draft # 94 and #95- Could we see the accent pink line in more of a brush stroke and could you make the logo a little bigger and the name and title smaller. Please add the website on the front of the card and add "Locally owned and operated" in the back.
draft #58
We would like to include our tag line of the front of the card "Making memories, one dip at a time!" Could we see this tagline in the same script font used in the logo. Could you also add
"Serving Bakersfield & Surrounding Areas" on the back of the card, above the watermark
Mossworks-Could we see the coordinating stationery and envelopes for draft #58
Thank you all for your submissions! We are off to a good start. Please show us more options using the chocolate brown as the primary color and using pink as the accent color. Also please remember to include "Locally owned and operated." on the back of the card. (without quotation marks, of course)
We would also like to see the fountain part of the logo or the initials as a watermark on the back of the card.
We want to make sure the font on the logo is bigger than the other font size used on the rest of the card.
Draft # 54 could we see the front logo a little bigger and add Locally owned and operated on the back.
Thanks!=)

```html
<!DOCTYPE html>
<html lang="en">
<head>
<meta charset="utf-8">
<title>Lila-Mae's Gourmet Fountains – Business Card</title>
<link href="https://fonts.googleapis.com/css2?family=Open+Sans:wght@400;600;700&display=swap" rel="stylesheet">
<style>
  :root {
    --backdrop: #ece7e1;
    --card-white: #ffffff;
    --crimson: #c42a55;
    --pink-light: #e27898;
    --maroon: #5a1420;
    --grey-text: #6b6b6b;
    --brown: #4a2418;
  }
  html, body {
    margin: 0;
    width: 1200px;
    height: 931px;
    overflow: hidden;
    background: var(--backdrop);
    font-family: "Open Sans", Arial, sans-serif;
  }
  .business-card {
    position: absolute;
    left: 100px;
    top: 180px;
    width: 1000px;
    height: 570px;
    border-radius: 40px;
    overflow: hidden;
    background: var(--card-white);
    box-shadow: 0 10px 30px rgba(60, 30, 20, 0.18);
  }
  .card-band {
    position: absolute;
    inset: 0;
  }
  .holder {
    position: absolute;
    right: 60px;
    top: 42px;
    text-align: right;
  }
  .holder-name {
    margin: 0;
    font-size: 30px;
    font-weight: 700;
    color: var(--crimson);
    line-height: 1.1;
  }
  .holder-title {
    margin: 2px 0 0;
    font-size: 18px;
    color: var(--grey-text);
  }
  .brand {
    position: absolute;
    left: 200px;
    top: 150px;
    display: flex;
    align-items: center;
    gap: 16px;
  }
  .brand-dot {
    width: 34px;
    height: 34px;
    border-radius: 50%;
    background: var(--crimson);
  }
  .brand-name {
    margin: 0;
    font-size: 38px;
    font-weight: 600;
    color: var(--brown);
    line-height: 1.15;
  }
  .contact {
    position: absolute;
    left: 280px;
    width: 620px;
    top: 440px;
    text-align: center;
    color: #ffffff;
    font-size: 19px;
    line-height: 1.6;
  }
  .contact p { margin: 0; }
  .contact b { font-weight: 700; }
</style>
</head>
<body>
  <div class="business-card">
    <svg class="card-band" viewBox="0 0 1000 570" width="1000" height="570" aria-hidden="true">
      <defs>
        <linearGradient id="band-pink" x1="0" y1="0" x2="1" y2="0.4">
          <stop offset="0" stop-color="#b82450"/>
          <stop offset="0.5" stop-color="#e27898"/>
          <stop offset="1" stop-color="#c42a55"/>
        </linearGradient>
      </defs>
      <path fill="var(--maroon)" d="M0,300 C220,285 420,372 600,350 C760,330 900,255 1000,222 L1000,236 C900,268 780,342 620,362 C450,385 250,325 0,332 Z"/>
      <path fill="url(#band-pink)" d="M0,332 C250,325 450,385 620,362 C780,342 900,268 1000,236 L1000,570 L0,570 Z"/>
    </svg>

    <div class="holder">
      <p class="holder-name">Rosa Delgado</p>
      <p class="holder-title">Owner</p>
    </div>

    <div class="brand">
      <span class="brand-dot"></span>
      <p class="brand-name">Lila-Mae's<br>Gourmet Fountains</p>
    </div>

    <div class="contact">
      <p><b>Phone :</b> 555-201-4870 <b>Fax :</b> 555-201-4871</p>
      <p><b>Email :</b> rosa@lilamaes.com <b>Web :</b> www.lilamaes.com</p>
    </div>
  </div>
</body>
</html>
```